Business Card Design

I need a business card design. I am a sole practitioner.I am a psychotherapist and I need a professional card. I am also an art therapist (a form of psychotherapy using art) so I want the image to be professional/creative/maybe ethnic. I do not want a boring minimalist "medical" image, nor do I want it too hippy/tree hugging.
Colours like reds/ochres/yellows would be good.
Industry/Entity Type
Business
Contact Information for Business Card
Mira Tanvel
Psychotherapy, Counselling and Art Therapy
Korrabel Lodge Counselling and Wellbeing services
17 Farrow Lane, Pelbury 4091
0419362750 www.MiraTanvel.com.au
on rear of card I need the option to have at least 4 or 5 appointment times /dates
Look and feel
Each slider illustrates characteristics of the customer's brand and the style your logo design should communicate.

```html
<!DOCTYPE html>
<html lang="en">
<head>
<meta charset="utf-8">
<title>Mira Tanvel Psychotherapy – Business Card</title>
<link rel="stylesheet" href="https://fonts.googleapis.com/css2?family=Libre+Baskerville:wght@700&family=Saira+Semi+Condensed:wght@300;400&display=swap">
<style>
  :root {
    --page: #d8d9dc;
    --card: #ffffff;
    --sage: #7b8a7b;
    --sage-light: #93a58a;
    --sage-dark: #687668;
    --panel: #ececec;
    --ink: #3a3f3a;
    --logo-ink: #4b5a4b;
    --accent: #8fa07f;
    --on-sage: #f4f6f2;
  }
  * { margin: 0; padding: 0; box-sizing: border-box; }
  html, body {
    width: 1200px; height: 1082px; overflow: hidden;
    background: var(--page);
  }
  .business-card {
    position: absolute; left: 75px; top: 241px;
    width: 1050px; height: 600px;
    background: var(--card);
    overflow: hidden;
    box-shadow: 0 6px 18px rgba(0,0,0,0.18);
  }
  .card-shapes { position: absolute; inset: 0; }
  .holder {
    position: absolute; left: 330px; top: 52px;
    font-family: "Saira Semi Condensed", sans-serif;
    color: var(--on-sage);
    display: flex; align-items: center; gap: 20px;
  }
  .holder-name { font-size: 38px; font-weight: 400; letter-spacing: 4px; }
  .holder-divider { width: 3px; height: 34px; background: var(--on-sage); }
  .holder-role { font-size: 22px; font-weight: 300; letter-spacing: 3px; }
  .brand {
    position: absolute; left: 420px; top: 215px;
    display: flex; align-items: center; gap: 22px;
  }
  .brand-dot {
    width: 74px; height: 74px; border-radius: 50%;
    background: var(--accent);
  }
  .brand-name {
    font-family: "Libre Baskerville", serif;
    font-weight: 700; font-size: 32px; color: var(--logo-ink);
  }
  .brand-tagline {
    font-family: "Saira Semi Condensed", sans-serif;
    font-weight: 400; font-size: 24px; color: var(--accent);
    margin-top: 4px; letter-spacing: 0.5px;
  }
  .address {
    position: absolute; left: 470px; top: 480px;
    font-family: "Saira Semi Condensed", sans-serif;
    font-size: 34px; font-weight: 400; letter-spacing: 2px;
    color: var(--on-sage);
  }
  .contact-list {
    position: absolute; left: 40px; top: 218px;
    list-style: none;
    font-family: "Saira Semi Condensed", sans-serif;
    font-size: 21px; color: var(--ink); letter-spacing: 0.5px;
  }
  .contact-list li { display: flex; align-items: center; gap: 14px; height: 36px; }
  .contact-list svg { width: 20px; height: 20px; fill: none; stroke: var(--ink); stroke-width: 1.8; }
</style>
</head>
<body>
  <article class="business-card">
    <svg class="card-shapes" viewBox="0 0 1050 600" width="1050" height="600" aria-hidden="true">
      <rect class="band-top" x="0" y="0" width="1050" height="150" fill="var(--sage)"/>
      <polygon class="band-top-facet" points="0,0 300,150 0,150" fill="var(--sage-light)"/>
      <rect class="contact-panel" x="0" y="150" width="370" height="260" fill="var(--panel)"/>
      <rect class="band-bottom" x="0" y="410" width="1050" height="190" fill="var(--sage)"/>
      <polygon class="band-bottom-facet" points="0,600 0,420 370,290 370,410 520,600" fill="var(--sage-light)" opacity="0.85"/>
      <polygon class="band-bottom-shade" points="760,410 1050,410 1050,600 900,600" fill="var(--sage-dark)" opacity="0.45"/>
    </svg>

    <div class="holder">
      <span class="holder-name">MIRA TANVEL</span>
      <span class="holder-divider"></span>
      <span class="holder-role">GENERAL MANAGER</span>
    </div>

    <div class="brand">
      <span class="brand-dot"></span>
      <div>
        <div class="brand-name">Mira Tanvel Psychotherapy</div>
        <div class="brand-tagline">Counselling and Art Therapy</div>
      </div>
    </div>

    <ul class="contact-list">
      <li><svg viewBox="0 0 20 20"><path d="M5 2l3 4-2 2c1 3 3 5 6 6l2-2 4 3-2 3C9 18 2 11 2 4z"/></svg>0419 362 750</li>
      <li><svg viewBox="0 0 20 20"><rect x="5" y="2" width="10" height="16" rx="2"/><line x1="9" y1="15" x2="11" y2="15"/></svg>0419 362 750</li>
      <li><svg viewBox="0 0 20 20"><rect x="2" y="8" width="16" height="10" rx="1"/><rect x="5" y="2" width="10" height="6"/></svg>0419 362 750</li>
      <li><svg viewBox="0 0 20 20"><rect x="2" y="4" width="16" height="12" rx="1"/><path d="M2 5l8 6 8-6"/></svg>hello@miratanvel.com.au</li>
      <li><svg viewBox="0 0 20 20"><circle cx="10" cy="10" r="8"/><ellipse cx="10" cy="10" rx="3.5" ry="8"/><line x1="2" y1="10" x2="18" y2="10"/></svg>www.MiraTanvel.com.au</li>
    </ul>

    <div class="address">17 Farrow Lane, Pelbury 4091</div>
  </article>
</body>
</html>
```